Cover for Where the Quiet River Bends Beyond Our Morning

Cover for a book that describes everything that happens to a person, from pre-birth life plans through growing in compassion and wisdom to death and living in the afterlife. The information is revealed in messages from people living in the life after this life. The title is Lanterns Along the Hidden Stair of Every Soul: Gathered from Voices Dwelling in the Further Meadow. Author is T. Morven Ashdale. Book size is 6 by 9.

Target Market(s)

General

Font styles to use
Serif

```html
<!DOCTYPE html>
<html lang="en">
<head>
<meta charset="utf-8">
<title>Lanterns Along the Hidden Stair of Every Soul — Book Cover</title>
<link rel="stylesheet" href="https://fonts.googleapis.com/css2?family=Alfa+Slab+One&family=Bowlby+One&display=swap">
<style>
  :root {
    --page-bg: #ece6dc;
    --ink-white: #ffffff;
    --shadow: rgba(40, 10, 15, 0.75);
    --maroon: #4a2a31;
    --deep-maroon: #3c2228;
    --crimson: #8a1f22;
    --glow-green: #3c9a5a;
    --glow-yellow: #d8b22a;
    --ember: #d9661c;
  }
  * { box-sizing: border-box; margin: 0; padding: 0; }
  html, body {
    width: 1200px;
    height: 995px;
    overflow: hidden;
    background: var(--page-bg);
  }
  .stage {
    width: 1200px;
    height: 995px;
    display: flex;
    align-items: center;
    justify-content: center;
  }
  .book-cover {
    position: relative;
    width: 610px;
    height: 915px;
    overflow: hidden;
    background: var(--maroon);
    box-shadow: 0 10px 30px rgba(0,0,0,0.25);
  }
  .cover-art {
    position: absolute;
    inset: 0;
    background:
      radial-gradient(ellipse 40% 22% at 45% 62%, rgba(216,178,42,0.75), transparent 70%),
      radial-gradient(ellipse 55% 30% at 55% 52%, rgba(60,154,90,0.85), transparent 72%),
      radial-gradient(ellipse 60% 12% at 60% 97%, rgba(217,102,28,0.8), transparent 70%),
      linear-gradient(100deg, transparent 10%, rgba(138,31,34,0.55) 18%, transparent 26%, transparent 55%, rgba(138,31,34,0.5) 63%, transparent 72%),
      linear-gradient(180deg, var(--maroon) 0%, #5a2a2c 30%, #4d4a2e 55%, var(--deep-maroon) 72%, var(--deep-maroon) 88%, #6a2e20 100%);
  }
  .cover-text {
    position: absolute;
    inset: 0;
    color: var(--ink-white);
    text-align: center;
  }
  .author {
    position: absolute;
    top: 50px;
    left: 0;
    right: 0;
    font-family: "Alfa Slab One", serif;
    font-size: 23px;
    line-height: 1;
    letter-spacing: 0.4em;
    padding-left: 0.4em;
    white-space: nowrap;
  }
  .title {
    position: absolute;
    top: 98px;
    left: 0;
    right: 0;
    font-family: "Bowlby One", serif;
    font-weight: 400;
    text-shadow: 3px 4px 3px var(--shadow);
    line-height: 1;
    white-space: nowrap;
  }
  .title-lead {
    display: block;
    font-size: 80px;
  }
  .title-rest {
    display: block;
    margin-top: 10px;
    font-size: 44px;
    line-height: 1.1;
  }
  .title-rest .small-line {
    display: block;
    font-size: 33px;
  }
  .subtitle-box {
    position: absolute;
    left: 55px;
    top: 640px;
    width: 500px;
    height: 120px;
  }
  .subtitle-frame {
    position: absolute;
    inset: 0;
  }
  .subtitle {
    position: absolute;
    inset: 0;
    display: flex;
    flex-direction: column;
    align-items: center;
    justify-content: center;
    font-family: "Bowlby One", serif;
    font-size: 21px;
    line-height: 1.35;
    white-space: nowrap;
  }
  .subtitle span { display: block; }
</style>
</head>
<body>
  <main class="stage">
    <section class="book-cover">
      <div class="cover-art" role="img" aria-label="Photograph of a dramatic sky: dark storm clouds with glowing yellow edges and green and red light rays streaming upward"></div>
      <div class="cover-text">
        <p class="author">T. MORVEN ASHDALE</p>
        <h1 class="title">
          <span class="title-lead">LANTERNS</span>
          <span class="title-rest">
            <span class="small-line">ALONG THE HIDDEN STAIR</span>
            OF EVERY SOUL
          </span>
        </h1>
        <div class="subtitle-box">
          <svg class="subtitle-frame" width="500" height="120" viewBox="0 0 500 120" aria-hidden="true">
            <g fill="none" stroke="#ffffff" stroke-width="4">
              <polyline points="110,90 8,90 8,4 492,4 492,30"/>
              <polyline points="80,116 492,116 492,88"/>
              <polyline points="8,102 8,116 40,116"/>
            </g>
          </svg>
          <p class="subtitle">
            <span>GATHERED FROM VOICES DWELLING</span>
            <span>IN THE FURTHER MEADOW</span>
          </p>
        </div>
      </div>
    </section>
  </main>
</body>
</html>
```